Educational non-profit needs an End of the Year Flyer

We need a flyer to mail to our supporters asking for donations to our program. Hillcrest Open Learning Hub runs after school programs for low-income students in Pasadena, CA. This is our end of the year mailing to supporters asking them to finish out the year with their contributions so that we can meet our budget.

Target Market(s)

Donors and supporters of organization

Industry/Entity Type

Non-Profit

Font styles to use
Serif

Colors

Designer to choose colors to be used in the design.

Requirements
Must have
• The project should fit on a 6x9" card, and be printed on front and back. It should show pictures, use the copy I have included, a space for a label address, a stamp, and the return address.
Nice to have
• eye-catching, fun

```html
<!DOCTYPE html>
<html lang="en">
<head>
<meta charset="utf-8">
<title>Hillcrest Open Learning Hub – End of Year Mailer</title>
<link rel="stylesheet" href="https://fonts.googleapis.com/css2?family=Permanent+Marker&family=Roboto+Slab:wght@300;400;700&family=Open+Sans:wght@300;700&display=swap">
<style>
  :root {
    --page: #ece9e4;
    --sky: #7fcbea;
    --band: #16a6d6;
    --grass: #2f9e3a;
    --grass-light: #4cbf4a;
    --headline: #e3212b;
    --donate: #1a9a45;
    --ink: #222222;
    --muted: #9a9a9a;
    --rule: #b9b9b9;
    --white: #ffffff;
  }
  * { box-sizing: border-box; margin: 0; padding: 0; }
  html, body { width: 1200px; height: 1000px; overflow: hidden; }
  body { background: var(--page); position: relative; font-family: "Roboto Slab", Georgia, serif; color: var(--ink); }

  .card { position: absolute; width: 720px; height: 480px; overflow: hidden; box-shadow: 0 2px 8px rgba(0,0,0,.15); }
  .card--front { left: 30px; top: 20px; background: var(--sky); }
  .card--back { left: 450px; top: 505px; background: var(--white); }

  /* front */
  .cloud, .sun, .flower, .photo { position: absolute; }
  .cloud { background: #f4f6f7; border-radius: 30px; }
  .sun { background: #f5d93a; border-radius: 50%; }
  .flower { width: 22px; height: 22px; border-radius: 50%; }
  .photo { background: linear-gradient(135deg, #7a6a5e, #c9a88c); border: 3px solid var(--white); box-shadow: 0 1px 3px rgba(0,0,0,.3); }
  .photo--indoor { background: linear-gradient(135deg, #5d4a3c, #b58e6d); }
  .photo--outdoor { background: linear-gradient(135deg, #8a8f6a, #d3c6a4); }
  .photo--hall { background: linear-gradient(135deg, #3f3a38, #8c6e5c); }

  .headline { position: absolute; left: 130px; top: 66px; width: 440px; text-align: center; font-family: "Permanent Marker", "Comic Sans MS", cursive; font-weight: 400; color: var(--headline); line-height: 1.1; letter-spacing: 1px; white-space: nowrap; }
  .headline__small { display: block; font-size: 36px; }
  .headline__large { display: block; font-size: 42px; }

  .grass { position: absolute; left: 0; top: 372px; width: 720px; height: 28px; background: linear-gradient(var(--grass-light), var(--grass)); }
  .band { position: absolute; left: 0; top: 398px; width: 720px; height: 82px; background: var(--band); }

  .brand { position: absolute; display: flex; align-items: center; gap: 6px; }
  .brand__dot { width: 14px; height: 14px; border-radius: 50%; }
  .brand__name { font-family: "Roboto Slab", Georgia, serif; font-weight: 700; }
  .brand--front { left: 14px; top: 22px; width: 100px; color: var(--white); font-size: 10px; line-height: 1.2; }
  .brand--front .brand__dot { background: var(--white); flex: none; }

  .band__address { position: absolute; left: 118px; top: 10px; color: var(--white); font-size: 13px; line-height: 1.7; font-style: normal; }
  .badge { position: absolute; left: 500px; top: 16px; width: 46px; height: 46px; border-radius: 50%; background: #d9b93a; }

  .donate { position: absolute; text-align: center; }
  .donate__label { font-family: "Open Sans", Arial, sans-serif; font-weight: 300; color: var(--muted); }
  .donate__button { display: block; background: var(--donate); color: var(--white); font-family: "Open Sans", Arial, sans-serif; font-weight: 700; border-radius: 30px; white-space: nowrap; }
  .payments { display: flex; justify-content: center; gap: 3px; }
  .payments span { background: var(--white); color: #2a4a8a; font-family: "Open Sans", Arial, sans-serif; font-weight: 700; border: 1px solid #cfcfcf; border-radius: 2px; }

  .donate--front { left: 560px; top: 2px; width: 152px; }
  .donate--front .donate__label { font-size: 10px; color: #d8eef7; }
  .donate--front .donate__button { font-size: 11px; padding: 7px 0; margin: 2px 0 4px; }
  .donate--front .payments span { font-size: 6px; padding: 1px 3px; }

  /* back */
  .letter { position: absolute; left: 18px; top: 8px; width: 316px; font-size: 12.5px; font-weight: 300; line-height: 1.28; text-align: justify; }
  .letter__ask { text-align: center; margin-top: 10px; }
  .letter__greeting { text-align: center; font-weight: 700; margin-top: 12px; font-size: 12px; }

  .donate--back { left: 58px; top: 252px; width: 236px; }
  .donate--back .donate__label { font-size: 14px; }
  .donate--back .donate__button { font-size: 17px; padding: 11px 0; margin: 2px 0 5px; }
  .donate--back .payments span { font-size: 7px; padding: 2px 4px; }

  .contact { position: absolute; left: 30px; top: 372px; list-style: none; font-size: 8px; line-height: 1; }
  .contact li { display: flex; align-items: center; gap: 8px; height: 19px; }
  .contact svg { width: 11px; height: 11px; flex: none; }

  .mail-address { position: absolute; left: 360px; top: 14px; font-size: 12.5px; line-height: 1.9; font-style: normal; }
  .stamp { position: absolute; left: 618px; top: 10px; width: 72px; height: 82px; background: #e8e8e8; border: 2px solid #dcdcdc; }
  .label-lines { position: absolute; left: 362px; top: 100px; width: 330px; }
  .label-lines span { display: block; height: 26px; border-bottom: 1px solid var(--rule); }

  .brand--back { left: 480px; top: 360px; width: 150px; font-size: 13px; line-height: 1.25; color: var(--ink); }
  .brand--back .brand__dot { background: var(--ink); width: 16px; height: 16px; flex: none; }
</style>
</head>
<body>

<section class="card card--front" aria-label="Mailer front">
  <div class="cloud" style="left:70px;top:10px;width:90px;height:38px" role="img" aria-label="Cloud illustration"></div>
  <div class="cloud" style="left:588px;top:14px;width:70px;height:30px" role="img" aria-label="Cloud illustration"></div>
  <div class="sun" style="left:658px;top:2px;width:44px;height:44px" role="img" aria-label="Sun illustration"></div>

  <div class="flower" style="left:146px;top:176px;background:#e0562a" role="img" aria-label="Flower illustration"></div>
  <div class="flower" style="left:176px;top:232px;background:#f3d43b" role="img" aria-label="Flower illustration"></div>
  <div class="flower" style="left:236px;top:220px;background:#4a79d1" role="img" aria-label="Flower illustration"></div>
  <div class="flower" style="left:326px;top:248px;background:#d4683a" role="img" aria-label="Flower illustration"></div>
  <div class="flower" style="left:470px;top:230px;background:#f3d43b" role="img" aria-label="Flower illustration"></div>
  <div class="flower" style="left:534px;top:190px;background:#e0562a" role="img" aria-label="Flower illustration"></div>

  <h1 class="headline">
    <span class="headline__small">WE NEED YOUR HELP</span>
    <span class="headline__large">TO FINISH 2018</span>
    <span class="headline__large">STRONG !</span>
  </h1>

  <div class="photo photo--indoor" style="left:38px;top:92px;width:84px;height:84px" role="img" aria-label="Photo of a student holding up her schoolwork"></div>
  <div class="photo photo--hall" style="left:16px;top:188px;width:112px;height:66px" role="img" aria-label="Photo of students gathered in a hall"></div>
  <div class="photo photo--indoor" style="left:22px;top:262px;width:120px;height:90px" role="img" aria-label="Photo of students holding basketballs"></div>
  <div class="photo photo--indoor" style="left:142px;top:268px;width:114px;height:82px" role="img" aria-label="Photo of a group of students indoors"></div>
  <div class="photo photo--hall" style="left:256px;top:272px;width:114px;height:82px" role="img" aria-label="Photo of students in a classroom"></div>
  <div class="photo photo--outdoor" style="left:372px;top:262px;width:74px;height:94px" role="img" aria-label="Photo of a child on playground equipment"></div>
  <div class="photo photo--outdoor" style="left:446px;top:258px;width:118px;height:86px" role="img" aria-label="Photo of children on a swing outdoors"></div>
  <div class="photo photo--hall" style="left:570px;top:254px;width:118px;height:78px" role="img" aria-label="Photo of two children smiling"></div>
  <div class="photo photo--indoor" style="left:604px;top:80px;width:88px;height:70px" role="img" aria-label="Photo of children preparing food"></div>
  <div class="photo photo--hall" style="left:586px;top:176px;width:116px;height:68px" role="img" aria-label="Photo of a music performance on stage"></div>

  <div class="grass" role="img" aria-label="Grass illustration"></div>

  <footer class="band">
    <div class="brand brand--front">
      <span class="brand__dot"></span>
      <span class="brand__name">Hillcrest Open Learning Hub</span>
    </div>
    <address class="band__address">
      Hillcrest Open Learning Hub,<br>214 N. Alder Ave,<br>Pasadena, CA&nbsp; 91106
    </address>
    <div class="badge" aria-label="Anniversary badge"></div>
    <div class="donate donate--front">
      <span class="donate__label">Donate Online</span>
      <span class="donate__button">www.brightpath-kids.org</span>
      <div class="payments"><span>PayLink</span><span>Vantage</span><span>Meridian</span></div>
    </div>
  </footer>
</section>

<section class="card card--back" aria-label="Mailer back">
  <div class="letter">
    <p>We need your help to finish out 2018 strong! We have had a wonderful 25th year of serving the children and families of Pasadena here at Hillcrest Open Learning Hub with high quality afterschool programs.</p>
    <p>Hundreds and hundreds of students have been a part of the Bright Path Kids Club family. Our annual budget is $275,000 and we count on $100,000 from individual donors.</p>
    <p class="letter__ask">Will you join with us for an end of the year contribution?</p>
    <p class="letter__greeting">Merry Christmas from all of us at HOLH!</p>
  </div>

  <div class="donate donate--back">
    <span class="donate__label">Donate Online</span>
    <span class="donate__button">www.brightpath-kids.org</span>
    <div class="payments"><span>PayLink</span><span>Vantage</span><span>Meridian</span><span>Amity</span></div>
  </div>

  <ul class="contact">
    <li><svg viewBox="0 0 12 12"><path d="M6 0.5a4 4 0 0 0-4 4c0 3 4 7 4 7s4-4 4-7a4 4 0 0 0-4-4zm0 5.5a1.5 1.5 0 1 1 0-3 1.5 1.5 0 0 1 0 3z" fill="#e0322b"/></svg>Hillcrest Open Learning Hub, 214 N. Alder Ave, Pasadena, CA&nbsp; 91106</li>
    <li><svg viewBox="0 0 12 12"><path d="M2.5 1l2 2.2-1 1.3a7 7 0 0 0 4 4l1.3-1 2.2 2-1.3 1.8C5 11 1 7 .7 2.3z" fill="#e0322b"/></svg>(626) 555-0142</li>
    <li><svg viewBox="0 0 12 12"><path d="M1 2.5h10v7H1z" fill="none" stroke="#e0322b" stroke-width="1.2"/><path d="M1 2.5l5 4 5-4" fill="none" stroke="#e0322b" stroke-width="1.2"/></svg>info@brightpathkids.org</li>
    <li><svg viewBox="0 0 12 12"><rect x="1" y="1" width="10" height="10" rx="1.5" fill="#3b5a9a"/></svg>Hillcrest Open Learning Hub</li>
  </ul>

  <address class="mail-address">
    Hillcrest Open Learning Hub,<br>214 N. Alder Ave,<br>Pasadena, CA&nbsp; 91106
  </address>
  <div class="stamp" aria-label="Stamp area"></div>
  <div class="label-lines" aria-label="Address label area">
    <span></span><span></span><span></span><span></span><span></span>
  </div>

  <div class="brand brand--back">
    <span class="brand__dot"></span>
    <span class="brand__name">Hillcrest Open Learning Hub</span>
  </div>
</section>

</body>
</html>
```